Design business card for Bright Harbour Coaching!

I am a personal development coach (like a life coach) and corporate trainer and need a professionally designed double sided business card.

It needs to contain the business logo (I'm happy for the designer to choose the layout of the logo as I am still working out the best option myself) and the following information:

Corinne Vashti
Personal Development Coach and Trainer

+61 (0)452 918 637 (written that way)
corinne@bright-harbour.example

www.bright-harbour.example

```html
<!DOCTYPE html>
<html lang="en">
<head>
<meta charset="utf-8">
<title>Bright Harbour Coaching — Business Card</title>
<link rel="stylesheet" href="https://fonts.googleapis.com/css2?family=Cinzel:wght@400&family=Open+Sans:wght@400;600&display=swap">
<style>
  :root {
    --bg: #e9e6e1;
    --card-black: #0b0b0c;
    --card-black-soft: #1c1c1e;
    --teal: #0e95a3;
    --teal-dark: #087480;
    --teal-bright: #16a5b4;
    --silver: #b9b9b9;
    --white: #ffffff;
  }
  * { box-sizing: border-box; margin: 0; padding: 0; }
  html, body { width: 1200px; height: 900px; overflow: hidden; }
  body {
    background: var(--bg);
    font-family: "Open Sans", Arial, sans-serif;
    position: relative;
  }
  .card {
    position: absolute;
    width: 560px;
    height: 320px;
    left: 320px;
    border-radius: 4px;
    overflow: hidden;
    background: radial-gradient(ellipse at 50% 40%, var(--card-black-soft) 0%, var(--card-black) 75%);
    box-shadow: 0 10px 28px rgba(0,0,0,0.22);
  }
  .card--front { top: 90px; }
  .card--back { top: 470px; }

  /* Front */
  .brand {
    position: absolute;
    inset: 0;
    display: flex;
    flex-direction: column;
    align-items: center;
    justify-content: center;
    gap: 22px;
  }
  .brand__dot {
    width: 46px; height: 46px; border-radius: 50%;
    background: var(--teal);
  }
  .brand__name {
    font-family: "Cinzel", Georgia, serif;
    font-weight: 400;
    font-size: 30px;
    letter-spacing: 1px;
    color: var(--silver);
    text-align: center;
    line-height: 1.1;
  }

  /* Back */
  .wave { position: absolute; inset: 0; }
  .back-dot {
    position: absolute;
    right: 60px; top: 34px;
    width: 92px; height: 92px; border-radius: 50%;
    background: var(--teal);
  }
  .person {
    position: absolute;
    left: 36px; top: 58px;
  }
  .person__name {
    color: var(--teal-bright);
    font-weight: 600;
    font-size: 21px;
    line-height: 1.2;
  }
  .person__role {
    color: var(--white);
    font-size: 13px;
    margin-top: 2px;
  }
  .contact {
    position: absolute;
    left: 36px; top: 170px;
    list-style: none;
  }
  .contact__item {
    display: flex;
    align-items: center;
    gap: 10px;
    color: var(--white);
    font-size: 14px;
    line-height: 24px;
  }
  .contact__icon { width: 13px; height: 13px; flex: none; }
</style>
</head>
<body>

<section class="card card--front" aria-label="Card front">
  <div class="brand">
    <span class="brand__dot"></span>
    <p class="brand__name">Bright Harbour<br>Coaching</p>
  </div>
</section>

<section class="card card--back" aria-label="Card back">
  <svg class="wave" viewBox="0 0 560 320" width="560" height="320" aria-hidden="true">
    <path d="M0,262 C150,312 320,250 420,178 C470,142 520,118 560,112 L560,320 L0,320 Z" fill="var(--teal-dark)"/>
    <path d="M0,272 C160,318 330,262 430,190 C480,154 525,132 560,126 L560,320 L0,320 Z" fill="var(--card-black)"/>
    <path d="M0,280 C170,322 340,272 440,200 C490,166 530,146 560,140 L560,320 L0,320 Z" fill="var(--teal)"/>
  </svg>

  <span class="back-dot"></span>

  <div class="person">
    <h1 class="person__name">Corinne Vashti</h1>
    <p class="person__role">Personal Development Coach and Trainer</p>
  </div>

  <ul class="contact">
    <li class="contact__item">
      <svg class="contact__icon" viewBox="0 0 16 16" aria-hidden="true"><path fill="var(--teal-bright)" d="M3.6 1.5l2.2 2.6-1.3 1.6c.9 2 2.6 3.7 4.6 4.6l1.6-1.3 2.6 2.2-1.3 2.3C7 13.2 2.8 9 2.3 2.8z"/></svg>
      +61 (0)452 918 637
    </li>
    <li class="contact__item">
      <svg class="contact__icon" viewBox="0 0 16 16" aria-hidden="true"><rect x="1" y="3" width="14" height="10" fill="var(--teal-bright)"/><path d="M1.5 3.5L8 9l6.5-5.5" fill="none" stroke="var(--card-black)" stroke-width="1.4"/></svg>
      corinne@bright-harbour.example
    </li>
    <li class="contact__item">
      <svg class="contact__icon" viewBox="0 0 16 16" aria-hidden="true"><g fill="none" stroke="var(--teal-bright)" stroke-width="2"><rect x="1.5" y="6" width="7" height="4" rx="2" transform="rotate(-45 5 8)"/><rect x="7.5" y="6" width="7" height="4" rx="2" transform="rotate(-45 11 8)"/></g></svg>
      www.bright-harbour.example
    </li>
  </ul>
</section>

</body>
</html>
```